Briefpapier und Visitenkarten für Bayerisches Gasthaus mit Zimmer
Zielgruppe
Traditionelle Gaststätte im Zentrum einer Kleinstadt in Bayern. Direkt am Marktplatz. 10 Gästezimmer.
Bayerisch. Traditionell. Von junger Geschäftsführerin geführt, mit jungem Personal. Wir haben das Objekt erst vor Kurzem erworben und fangen gerade an.
Gerichte: Braten, Steaks, Brotzeiten, vegetarische und VEGANE Speisen
Getränke: Sehr bierlastig. Es war früher ein Brauereigasthaus. Heute gibts auch eine kleine feine Weinkarte.
Zielgruppe sind Einheimische und Touristen. Im Sommer kommen Radfahrer und Wanderer. Besonders angesprochen werden auch Kinder. Es gibt eine großzügige Spielecke.
Aufgabenstellung
Das Gasthaus heißt Eichel. Daher spielt der Eichel im Design auch eine wichtige Rolle.
Nachdem wir sehr familienorientiert sind, könnte ich mir auch eine Eichel-Familie vorstellen.
Visitenkarten und Briefpapier sollen alle wichtigen Infos enthalten, aber dabei sehr klar gehalten werden und nicht überladen sein. Mir ist ein schlichtes und ansprechendes Design wichtig. Es soll nicht verspielt sein.
Hier ist die Homepage:
www.eichel-gasthof-online.de
Info auf Briefpapier:
GASTHAUS EICHEL
Brennauer GmbH
Als Info auf Visitenkarte:
Gasthaus Eichel

```html
<!DOCTYPE html>
<html lang="de">
<head>
<meta charset="utf-8">
<title>Briefpapier – Gasthaus Eichel</title>
<link rel="stylesheet" href="https://fonts.googleapis.com/css2?family=Source+Sans+3:wght@400&display=swap">
<style>
  :root {
    --backdrop: #76777a;
    --paper: #ffffff;
    --accent: #a6c424;
    --accent-pale: #f5f7ea;
    --text: #6a6a6a;
    --text-dark: #5e5e5e;
  }
  * { margin: 0; padding: 0; box-sizing: border-box; }
  html, body { width: 900px; height: 1200px; overflow: hidden; }
  body {
    background: var(--backdrop);
    position: relative;
    font-family: "Source Sans 3", Arial, sans-serif;
    color: var(--text);
  }
  .letter-sheet {
    position: absolute;
    left: 56px; top: 43px;
    width: 788px; height: 1114px;
    background: var(--paper);
    overflow: hidden;
  }
  .backdrop-motif {
    position: absolute;
    left: 0; top: 278px;
    width: 788px; height: 836px;
    background: linear-gradient(180deg, rgba(245,247,234,0) 0%, var(--accent-pale) 35%, var(--accent-pale) 100%);
  }
  .brand {
    position: absolute;
    left: 0; top: 112px; width: 100%;
    text-align: center;
  }
  .brand-name {
    font-family: "Source Sans 3", Arial, sans-serif;
    font-weight: 400;
    font-size: 24px;
    letter-spacing: 4px;
    color: var(--text-dark);
    line-height: 1;
  }
  .sender-line {
    position: absolute;
    left: 94px; top: 187px;
    font-size: 7.8px; letter-spacing: 0.2px;
    white-space: nowrap;
  }
  .dot { color: var(--accent); }
  .contact-block {
    position: absolute;
    left: 594px; top: 184px;
    font-size: 10px; letter-spacing: 0.6px;
    line-height: 14.6px;
    font-style: normal;
  }
  .contact-row { position: relative; padding-left: 12px; white-space: nowrap; }
  .contact-row svg { position: absolute; left: 0; top: 2px; width: 8px; height: 10px; }
  .contact-row.gap { margin-top: 4px; }
  .contact-row.gap-sm { margin-top: 4px; }
  .fold-mark {
    position: absolute; left: 0;
    width: 19px; height: 1px; background: var(--accent);
  }
  .legal-footer {
    position: absolute;
    left: 0; top: 1056px; width: 100%;
    text-align: center;
    font-size: 10.8px; letter-spacing: 0.5px;
    line-height: 15px;
    color: var(--text);
  }
  .footer-rule {
    position: absolute; left: 339px; top: 1096px;
    width: 110px; height: 1.5px;
    background: var(--accent);
  }
</style>
</head>
<body>
  <main class="letter-sheet">
    <div class="backdrop-motif" role="img" aria-label="Große, zartgrüne Hintergrundfläche"></div>

    <header class="brand">
      <div class="brand-name">GASTHAUS EICHEL</div>
    </header>

    <p class="sender-line">GASTHAUS EICHEL <span class="dot">•</span> Brennauer GmbH <span class="dot">•</span> Lindenplatz 7 <span class="dot">•</span> 84085 Lindhausen</p>

    <address class="contact-block">
      <div class="contact-row">
        <svg viewBox="0 0 8 10"><path d="M4 0a3.6 3.6 0 0 0-3.6 3.6C.4 6.2 4 10 4 10s3.6-3.8 3.6-6.4A3.6 3.6 0 0 0 4 0zm0 5a1.4 1.4 0 1 1 0-2.8A1.4 1.4 0 0 1 4 5z" fill="var(--accent)"/></svg>
        GASTHAUS EICHEL
      </div>
      <div class="contact-row gap">Brennauer GmbH</div>
      <div class="contact-row">Lindenplatz 7</div>
      <div class="contact-row">84085 Lindhausen</div>
      <div class="contact-row gap-sm">
        <svg viewBox="0 0 10 10"><path d="M9 1.2C8 .3 6.8.6 6.2 1.3L5.6 2l1.4 1.3L6.2 4.5C5 5.6 4 7 3.4 8L2 7 1.1 7.9C.6 8.6 1.3 10 2.2 9.7 5.6 8.6 8.4 5.5 9.6 2.4 9.8 1.9 9.5 1.5 9 1.2z" fill="var(--accent)"/></svg>
        08765 4321
      </div>
      <div class="contact-row gap-sm">
        <svg viewBox="0 0 10 10"><text x="5" y="8.5" text-anchor="middle" font-size="10" font-weight="700" fill="var(--accent)" font-family="Arial, sans-serif">@</text></svg>
        info@eichel-gasthof-online.de
      </div>
      <div class="contact-row">
        <svg viewBox="0 0 10 10"><circle cx="5" cy="5" r="4.3" fill="none" stroke="var(--accent)" stroke-width="1.2"/><path d="M.8 5h8.4M5 .8v8.4" stroke="var(--accent)" stroke-width="1"/></svg>
        www.eichel-gasthof-online.de
      </div>
    </address>

    <div class="fold-mark" style="top:394px"></div>
    <div class="fold-mark" style="top:556px"></div>
    <div class="fold-mark" style="top:788px"></div>

    <footer class="legal-footer">
      <p>Steuernummer: USt.-IdNr. DE xxx <span class="dot">•</span> Handelsregister: ORT <span class="dot">•</span> Geschäftsführer: Vorname Nachname</p>
      <p>Bank: Musterbank <span class="dot">•</span> IBAN DExx xxxx xxxx xxxx xxxx xx <span class="dot">•</span> BIC XXXXXXX 1XXX <span class="dot">•</span> Kontoinhaber: Brennauer GmbH</p>
    </footer>
    <div class="footer-rule"></div>
  </main>
</body>
</html>
```